This is my scope and requirements:
Labelling project:
This is related to the Label project I also opened up. (The Brisk Owl Organic & Natural Soaps needs a good business card (Contest) )
I have attached an initial draft at a logo I tried to come up with for a business card and labelling/marketing. I am hoping that you can take this logo and 'run with it' to finesse it, make it look unique and professional. If you need to change it, I am open to ideas.
I find that labelling/packaging is hard for me to make it look 'professional' so I am coming to the experts!
I am looking for label designs for 2 different bottles and 2 different bar soaps:
1) Organic Bar Soap (2 possibilities: 1) Kraft 'cigar' band around soap with twine, 2) Kraft soap box with Kraft sticker Labels
2) Natural Olive Oil Based Bar Soap (labelling can be same as Organic but with distinct info)
3) Organic Hand Washes (clear square bottles, 250ml with natural pump)
4) Natural Olive Oil Based Body Wash (taper bottle 200ml with metal silver disc top caps)
I am a start up at home company making Organic and Natural Bar soaps, hand soaps, body washes.
All of my ingredients are organic or natural and will include natural essential oils, exfoliants, natural powders/colours, etc.
Some of the names are: Quillomé (feisty, energetic soap), Dunes (more of a sandalwood earthy tones with a sandalwood powder exfoliant), Frost (maybe changing this name - fresh scented), Amber Thyme (lemongrass/ginger, exfoliants), etc....
If you need more information, please let me know!
Please find attached: Kraft Paper I am looking at to possibly wrap the Bar Soaps in (I like the different colour concept and am trying to decide between diff colours of Ned Parrow paper to wrap around or plain kraft paper.. whichever the new logo concept will look best with.
The bottles I will be using for the hand soap (250ml square) and the body wash (200ml tapered)
OLD POST:
Hello! I am a start up business that is specializing in making luxury organic bar soaps, natural olive oil bar soaps, organic hand wash, natural olive oil body wash/shower gel that will include essential oils, exfoliants, natural powders, etc. (also accessories: wood soap dishes, etc) .. I am looking for a great designer that can provide me with the business card and labelling designs! I appreciate feedback, ideas on how I can receive a great design to help sell my products!
I am attaching my initial logo design that I would like to keep - but am looking for someone to 'finesse' it or make it more professional/unique looking.
Again, this is hand in hand with the business card project I submitted.
Thanks!
Verla
Updates
I am sorry for the lack of direction or Scope of the project. I am new at this board.
Labelling project:
I have attached an initial draft at a logo I tried to come up with for a business card and labelling/marketing. I am hoping that you can take this logo and 'run with it' to finesse it, make it look unique and professional.
If you need more information, please let me know.
Hello; I just wanted to let everyone know that if you feel that this brand needs a different logo, I am open to ideas (if you don't think the one I started with is ok). I am coming to the experts here!
Just to confirm also - this is related to the business card project, therefore, there are 2 projects, 2 payments! :)
Cheers
Industry/Entity Type
Business
Look and feel
Each slider illustrates characteristics of the customer's brand and the style your logo design should communicate.

```html
<!DOCTYPE html>
<html lang="en">
<head>
<meta charset="utf-8">
<title>The Brisk Owl – Bottle Labels</title>
<link rel="stylesheet" href="https://fonts.googleapis.com/css2?family=Bangers&family=Chewy&family=Short+Stack&display=swap">
<style>
  :root {
    --ink: #353234;
    --pink: #e8698a;
    --blush: #f4a7bd;
    --paper: #ffffff;
    --orange: #f08a2c;
    --taupe: #a89684;
    --leaf: #a8c043;
    --backdrop: #ffffff;
  }
  * { margin: 0; padding: 0; box-sizing: border-box; }
  html, body { width: 1200px; height: 726px; overflow: hidden; background: var(--backdrop); }
  .canvas { position: relative; width: 1200px; height: 726px; }

  .label {
    position: absolute; top: 221px; width: 178px; height: 376px;
    border: 6px solid; border-radius: 16px; overflow: hidden; text-align: center;
  }
  .label--hand-wash { left: 132px; background: var(--ink); border-color: var(--blush); color: var(--paper); }
  .label--body-wash { left: 513px; background: var(--paper); border-color: var(--blush); color: var(--ink); }
  .label--body-wash-pink { left: 911px; background: var(--blush); border-color: var(--ink); color: var(--ink); }

  .brand-dot {
    position: absolute; top: -22px; right: -18px; width: 76px; height: 76px; border-radius: 50%;
    background: var(--pink);
  }
  .label--body-wash-pink .brand-dot { background: var(--paper); }

  .brand {
    position: absolute; top: 14px; left: 0; right: 0;
    font-family: "Chewy", cursive; font-weight: 400; line-height: 0.95;
  }
  .brand span { display: block; }
  .brand__the { font-size: 20px; text-align: right; padding-right: 26px; position: relative; }
  .brand__first { font-size: 36px; margin-top: 6px; }
  .brand__second { font-size: 50px; }
  .label--hand-wash .brand { color: var(--paper); }

  .rule { position: absolute; left: 8px; right: 8px; border-top: 2px dotted; }
  .rule--top { top: 142px; }
  .rule--bottom { top: 207px; }
  .label--hand-wash .rule { border-color: var(--paper); }
  .label--body-wash .rule, .label--body-wash-pink .rule { border-color: var(--pink); }

  .product-type {
    position: absolute; top: 152px; left: 0; right: 0;
    font-family: "Bangers", sans-serif; letter-spacing: 0.3px; line-height: 1.55;
  }
  .product-type__line--small { font-size: 13px; }
  .product-type__line { font-size: 15px; display: block; }
  .label--hand-wash .product-type, .label--body-wash .product-type { color: var(--pink); }

  .scent {
    position: absolute; top: 250px; left: 0; right: 0;
    font-family: "Bangers", sans-serif; font-size: 21px; line-height: 1.05; letter-spacing: 0.5px;
  }
  .scent span { display: block; }
  .scent__amber { color: var(--orange); }
  .scent__thyme { color: var(--taupe); }
  .label--body-wash .scent { color: var(--leaf); top: 258px; }
  .label--body-wash-pink .scent { color: var(--paper); top: 258px; }

  .notes {
    position: absolute; top: 310px; left: 0; right: 0;
    font-family: "Short Stack", cursive; font-size: 12px; line-height: 1.35; text-transform: uppercase;
  }
  .label--hand-wash .notes { top: 308px; color: var(--paper); }
  .label--body-wash .notes { top: 300px; color: var(--leaf); }
  .label--body-wash-pink .notes { top: 300px; color: var(--ink); }
</style>
</head>
<body>
<main class="canvas">

  <section class="label label--hand-wash">
    <div class="brand-dot"></div>
    <h2 class="brand"><span class="brand__the">THE</span><span class="brand__first">BRISK</span><span class="brand__second">OWL</span></h2>
    <div class="rule rule--top"></div>
    <p class="product-type"><span class="product-type__line product-type__line--small">ORGANIC</span><span class="product-type__line">HAND WASHES</span></p>
    <div class="rule rule--bottom"></div>
    <h3 class="scent"><span class="scent__amber">AMBER</span><span class="scent__thyme">THYME</span></h3>
    <p class="notes">Lemongrass<br>Ginger<br>Exfoliants</p>
  </section>

  <section class="label label--body-wash">
    <div class="brand-dot"></div>
    <h2 class="brand"><span class="brand__the">THE</span><span class="brand__first">BRISK</span><span class="brand__second">OWL</span></h2>
    <div class="rule rule--top"></div>
    <p class="product-type"><span class="product-type__line product-type__line--small">NATURAL OLIVE OIL BASED</span><span class="product-type__line">BODY WASH</span></p>
    <div class="rule rule--bottom"></div>
    <h3 class="scent">QUILLOMÉ</h3>
    <p class="notes">Feisty<br>Energetic Soap</p>
  </section>

  <section class="label label--body-wash-pink">
    <div class="brand-dot"></div>
    <h2 class="brand"><span class="brand__the">THE</span><span class="brand__first">BRISK</span><span class="brand__second">OWL</span></h2>
    <div class="rule rule--top"></div>
    <p class="product-type"><span class="product-type__line product-type__line--small">NATURAL OLIVE OIL BASED</span><span class="product-type__line">BODY WASH</span></p>
    <div class="rule rule--bottom"></div>
    <h3 class="scent">QUILLOMÉ</h3>
    <p class="notes">Feisty<br>Energetic Soap</p>
  </section>

</main>
</body>
</html>
```